Web Button design and production

I need remote control like buttons (or your own design of buttons if I like it)
3x4 text buttons (normal, pressed, disabled)
3x1 empty button (normal, pressed, disabled)
3x6 buttons with glyph (normal, pressed, disabled)
3x288 with 24h time "00:00", "00:05", "00:10" (normal, pressed, disabled)
4 LED (red, green, orange, black)
I will upload the background image as soon as possible (black plastic)
See attached images
Q: Do the buttons have to be gray/black?
A: It should look like a high end remote control. It could be brushed aluminum as well, or something you come up with. But I guess black or dark grey would be best. The background will be picsharbor 40561739, but it's not available yet.
Q: Do I have to provide all buttons for the contest?
A: No! I only need one button (3 states) and a LED to decide. Only the winner will do the whole job.
Q: Is the Designer who wins the contest expected to complete all the extra buttons?
A: Yes, please.
Plastic

```html
<!DOCTYPE html>
<html lang="en">
<head>
<meta charset="utf-8">
<title>Remote Control Web Buttons</title>
<link rel="stylesheet" href="https://fonts.googleapis.com/css2?family=Roboto:wght@400&display=swap">
<style>
  :root {
    --bg: #1c1c1c;
    --bg-light: #262626;
    --face-top: #4a4a4a;
    --face-mid: #1a1a1a;
    --face-bottom: #0a0a0a;
    --rim-top: #f2f2f2;
    --rim-mid: #9a9a9a;
    --rim-bottom: #5a5a5a;
    --label: #f4f4f4;
    --glyph: #ffffff;
    --led-yellow: #f2c21b;
    --led-green: #3fae3a;
    --led-red: #d5221c;
    --led-off: #cfcfcf;
  }
  * { box-sizing: border-box; margin: 0; padding: 0; }
  html, body { width: 1200px; height: 1200px; overflow: hidden; }
  body {
    background:
      radial-gradient(ellipse at 50% 40%, var(--bg-light) 0%, var(--bg) 70%),
      var(--bg);
    font-family: "Roboto", Arial, sans-serif;
    position: relative;
  }
  .key {
    position: absolute;
    border-radius: 20px;
    border: 6px solid transparent;
    background:
      linear-gradient(180deg, var(--face-top) 0%, var(--face-mid) 48%, var(--face-bottom) 100%) padding-box,
      linear-gradient(180deg, var(--rim-top) 0%, var(--rim-mid) 50%, var(--rim-bottom) 100%) border-box;
    box-shadow: 0 6px 10px rgba(0,0,0,.6), inset 0 0 0 2px rgba(0,0,0,.7);
    display: flex; align-items: center; justify-content: center;
    color: var(--label);
    overflow: hidden;
  }
  .key::before {
    content: "";
    position: absolute; left: 4px; right: 4px; top: 3px; height: 46%;
    border-radius: 14px 14px 40% 40% / 14px 14px 18px 18px;
    background: linear-gradient(180deg, rgba(255,255,255,.22), rgba(255,255,255,.04));
    pointer-events: none;
  }
  .key-time { width: 162px; height: 96px; font-size: 33px; letter-spacing: 1px; }
  .key-text { font-size: 33px; line-height: 1.1; text-align: center; text-transform: uppercase; }
  .key-login { font-size: 30px; text-transform: uppercase; }
  .key svg { width: 46px; height: 46px; fill: var(--glyph); position: relative; }
  .led {
    position: absolute; width: 81px; height: 81px;
    border-radius: 16px; border: 5px solid transparent;
    background:
      linear-gradient(180deg, #3a3a3a, #0b0b0b) padding-box,
      linear-gradient(180deg, var(--rim-top), var(--rim-bottom)) border-box;
    box-shadow: 0 4px 8px rgba(0,0,0,.6);
    display: flex; align-items: center; justify-content: center;
  }
  .led svg { width: 44px; height: 44px; }
  .led-yellow { color: var(--led-yellow); }
  .led-green { color: var(--led-green); }
  .led-red { color: var(--led-red); }
  .led-off { color: var(--led-off); }
</style>
</head>
<body>
  <div class="key key-time" style="left:204px;top:144px">23:15</div>
  <div class="key key-time" style="left:540px;top:90px">00:15</div>
  <div class="key key-text" style="left:384px;top:231px;width:246px;height:159px">Book<br>Now</div>
  <div class="key key-text" style="left:657px;top:231px;width:246px;height:159px">Jetzt<br>Buchen</div>
  <div class="key key-time" style="left:936px;top:267px;height:99px">00:10</div>
  <div class="key key-time" style="left:198px;top:309px">01:15</div>

  <div class="key" style="left:390px;top:429px;width:165px;height:159px" aria-label="Previous">
    <svg viewBox="0 0 40 40"><path d="M26 10 L12 20 L26 30 Z"/></svg>
  </div>
  <div class="key" style="left:735px;top:429px;width:162px;height:159px" aria-label="Next">
    <svg viewBox="0 0 40 40"><path d="M14 10 L28 20 L14 30 Z"/></svg>
  </div>

  <div class="led led-yellow" style="left:951px;top:450px">
    <svg viewBox="0 0 40 40" fill="none" stroke="currentColor" stroke-width="4" stroke-linecap="round"><circle cx="12" cy="28" r="3.5" fill="currentColor" stroke="none"/><path d="M11 19 A10 10 0 0 1 21 29"/><path d="M11 11 A18 18 0 0 1 29 29"/></svg>
  </div>
  <div class="led led-green" style="left:951px;top:558px">
    <svg viewBox="0 0 40 40" fill="none" stroke="currentColor" stroke-width="4" stroke-linecap="round"><circle cx="12" cy="28" r="3.5" fill="currentColor" stroke="none"/><path d="M11 19 A10 10 0 0 1 21 29"/><path d="M11 11 A18 18 0 0 1 29 29"/></svg>
  </div>
  <div class="led led-red" style="left:951px;top:660px">
    <svg viewBox="0 0 40 40" fill="none" stroke="currentColor" stroke-width="4" stroke-linecap="round"><circle cx="12" cy="28" r="3.5" fill="currentColor" stroke="none"/><path d="M11 19 A10 10 0 0 1 21 29"/><path d="M11 11 A18 18 0 0 1 29 29"/></svg>
  </div>

  <div class="key" style="left:396px;top:633px;width:162px;height:96px" aria-label="Back">
    <svg viewBox="0 0 40 40"><path d="M6 20 L18 10 L18 16 L34 16 L34 24 L18 24 L18 30 Z"/></svg>
  </div>
  <div class="key key-login" style="left:600px;top:633px;width:168px;height:96px">Login</div>
  <div class="led led-off" style="left:828px;top:639px;width:78px">
    <svg viewBox="0 0 40 40" fill="none" stroke="currentColor" stroke-width="4" stroke-linecap="round"><circle cx="12" cy="28" r="3.5" fill="currentColor" stroke="none"/><path d="M11 19 A10 10 0 0 1 21 29"/><path d="M11 11 A18 18 0 0 1 29 29"/></svg>
  </div>

  <div class="key" style="left:396px;top:753px;width:171px;height:96px" aria-label="Skip back">
    <svg viewBox="0 0 40 40"><rect x="9" y="9" width="5" height="22"/><path d="M31 9 L15 20 L31 31 Z"/></svg>
  </div>
  <div class="key" style="left:600px;top:753px;width:168px;height:96px" aria-label="Skip forward">
    <svg viewBox="0 0 40 40"><path d="M9 9 L25 20 L9 31 Z"/><rect x="26" y="9" width="5" height="22"/></svg>
  </div>
  <div class="key" style="left:786px;top:753px;width:165px;height:96px" aria-label="Return">
    <svg viewBox="0 0 40 40"><path d="M4 26 L15 16 L15 22 L26 22 Q30 22 30 18 L30 8 L36 8 L36 20 Q36 30 26 30 L15 30 L15 36 Z"/></svg>
  </div>
  <div class="key" style="left:786px;top:879px;width:165px;height:99px" aria-label="Blank button"></div>

  <div class="key key-time" style="left:312px;top:924px;width:168px">00:00</div>
  <div class="key key-time" style="left:507px;top:930px;width:165px">00:05</div>
</body>
</html>
```